Not another boring Business Card Design Project

This is not another boring Business Card Design Project.

We are looking for the weirdest, wackiest most boundary pushing designs that you can come up with.

If you believe that design can be fun, energetic, crazy, unpredictable, beautiful and eye-catching then read on… this project is for you.

We are Tolvin Presk and we print plastic cards.

We are running a Plastic Card Design Competition.

And we need a plastic card to advertise the competition to graphic designers just like you.

The design needs to make your average designers’ jaws drop and their eyes pop out.

You can do what you wish with the card design, so long as it stands out.

We like these designs, designs that stretch the boundaries and become something beyond just another business card:

http://quorvamedia.net/wp-content/uploads/2009/03/b48.jpg
Designer - http://www.pelvanworks.com/

http://quorvamedia.net/wp-content/uploads/2009/03/b41.jpg
Designer - http://renolbrakstad.com/

http://images.plinthhive.com/designs/44195_732292_37774_thumbnail.jpg
Designer- Zentro Media at Plinth Hive

http://images.plinthhive.com/designs/44195_717529_37774_thumbnail.jpg
Designer - Zentro Media at Plinth Hive

http://quorvamedia.net/wp-content/uploads/2009/03/b11.jpg
Designer - http://www.wk7studio.com/

http://quorvamedia.net/wp-content/uploads/2009/03/b16.jpg
Designer - http://www.pebbletumbler.com/

Reason: A number of designers have said they want to submit designs and haven't yet done so, we want to give them time.

Reason: We've extended the deadline by 4 days for those who want to submit their designs over the weekend and give ourselves time to judge them

Plastic

• The design needs to contain this link: lnk.example/QzRpLk and any other detail that will encourage competition entry. The design will be printed on plastic.
• No borders (when plastic cards are punched to shape and size there is movement of 1 - 2mm, borders highlight this movement).

Keep text 3mm away from edges of the cards.

Please don't create designs to be produced on clear/transparent plastic.

```html
<!DOCTYPE html>
<html lang="en">
<head>
<meta charset="utf-8">
<title>Don't be afraid to let yourself shine</title>
<link rel="stylesheet" href="https://fonts.googleapis.com/css2?family=Inter:wght@300;400&family=Pinyon+Script&family=Ruge+Boogie&display=swap">
<style>
  :root {
    --night-top: #e9e9e9;
    --night-mid: #6a6a6a;
    --night: #000000;
    --sea-top: #4cb2cb;
    --sea-bottom: #ffffff;
    --gold: #c98a33;
    --gold-light: #f3c683;
    --moon: #ffffff;
    --moon-halo: #8a8580;
    --sun-glow: #d9eef6;
    --text-light: #ffffff;
  }
  * { margin: 0; padding: 0; box-sizing: border-box; }
  html, body {
    width: 1200px;
    height: 627px;
    overflow: hidden;
    background: #ffffff;
  }
  .card {
    position: relative;
    width: 1200px;
    height: 627px;
    overflow: hidden;
  }
  .sky {
    position: absolute;
    left: 0; top: 0;
    width: 1200px; height: 310px;
    background: linear-gradient(to bottom, var(--night-top) 0px, var(--night-mid) 40px, var(--night) 110px, var(--night) 100%);
  }
  .sea {
    position: absolute;
    left: 0; top: 310px;
    width: 1200px; height: 317px;
    background: linear-gradient(to bottom, var(--sea-top) 0%, #8ccde0 45%, var(--sea-bottom) 100%);
  }
  .orb { position: absolute; }
  .orb--moon { left: 10px; top: 7px; }
  .orb--sun { left: 1031px; top: 438px; }
  .headline {
    position: absolute;
    left: 282px;
    top: 73px;
    color: var(--text-light);
    font-family: "Inter", "Helvetica Neue", Arial, sans-serif;
    font-weight: 300;
    font-size: 100px;
    letter-spacing: -1px;
    white-space: nowrap;
  }
  .headline__accent {
    position: absolute;
    left: 714px;
    top: 122px;
    color: var(--text-light);
    font-family: "Pinyon Script", cursive;
    font-size: 68px;
    white-space: nowrap;
  }
  .entry-link {
    position: absolute;
    left: 0;
    width: 1200px;
    top: 263px;
    text-align: center;
    color: var(--gold-light);
    -webkit-text-stroke: 1.5px var(--gold);
    font-family: "Inter", "Helvetica Neue", Arial, sans-serif;
    font-weight: 400;
    font-size: 64px;
    letter-spacing: -0.5px;
    white-space: nowrap;
  }
  .tagline {
    position: absolute;
    left: 132px;
    top: 391px;
    color: var(--gold);
    font-family: "Inter", "Helvetica Neue", Arial, sans-serif;
    font-weight: 300;
    font-size: 100px;
    letter-spacing: -1px;
    white-space: nowrap;
  }
  .tagline__accent {
    position: absolute;
    left: 768px;
    top: 368px;
    color: var(--gold);
    font-family: "Ruge Boogie", cursive;
    font-size: 144px;
    white-space: nowrap;
  }
</style>
</head>
<body>
  <main class="card">
    <div class="sky"></div>
    <div class="sea"></div>

    <svg class="orb orb--moon" width="176" height="176" viewBox="-88 -88 176 176" aria-hidden="true">
      <polygon fill="var(--moon-halo)" opacity="0.85"
        points="0,-84 9,-64 24,-80 26,-59 44,-71 40,-50 60,-57 51,-38 72,-40 58,-24 79,-21 62,-9 82,0 62,9 79,21 58,24 72,40 51,38 60,57 40,50 44,71 26,59 24,80 9,64 0,84 -9,64 -24,80 -26,59 -44,71 -40,50 -60,57 -51,38 -72,40 -58,24 -79,21 -62,9 -82,0 -62,-9 -79,-21 -58,-24 -72,-40 -51,-38 -60,-57 -40,-50 -44,-71 -26,-59 -24,-80 -9,-64"/>
      <circle r="58" fill="var(--moon)" stroke="var(--gold)" stroke-width="2"/>
    </svg>

    <svg class="orb orb--sun" width="176" height="176" viewBox="-88 -88 176 176" aria-hidden="true">
      <polygon fill="var(--sun-glow)" opacity="0.9"
        points="0,-84 9,-64 24,-80 26,-59 44,-71 40,-50 60,-57 51,-38 72,-40 58,-24 79,-21 62,-9 82,0 62,9 79,21 58,24 72,40 51,38 60,57 40,50 44,71 26,59 24,80 9,64 0,84 -9,64 -24,80 -26,59 -44,71 -40,50 -60,57 -51,38 -72,40 -58,24 -79,21 -62,9 -82,0 -62,-9 -79,-21 -58,-24 -72,-40 -51,-38 -60,-57 -40,-50 -44,-71 -26,-59 -24,-80 -9,-64"/>
      <circle r="60" fill="var(--gold)" stroke="#ffffff" stroke-width="2"/>
    </svg>

    <h1 class="headline">Don’t be</h1>
    <span class="headline__accent">afraid</span>

    <p class="entry-link">lnk.example/QzRpLk</p>

    <p class="tagline">to let yourself</p>
    <span class="tagline__accent">Shine</span>
  </main>
</body>
</html>
```